Copper Ridge Business Cards For New Startup

I am looking for you to design some business cards for a new startup https://copperridgehub.example. I have supplied logo, brand guidelines and our signatures as a guide.

We need this to reflect the brand guidelines and the website for brand consistency,

What is Copper Ridge?

Mallorca's Business Growth Community
Join your new business community full of passionate entrepreneurs who
love to solve problems and help each other grow together!

Any questions you can ask.

Target Market(s)

Business to Business

Contact Information for Business Card

These are attached (signatures) to the job

Font styles to use
Other font styles liked:
• Open Sans

Requirements
Must have
• Match design guidelines
Nice to have
• Photos of our faces so people remember us

```html
<!DOCTYPE html>
<html lang="en">
<head>
<meta charset="utf-8">
<title>Copper Ridge – Business Cards</title>
<link rel="stylesheet" href="https://fonts.googleapis.com/css2?family=Montserrat:wght@700&family=Open+Sans:wght@400;600&display=swap">
<style>
  :root {
    --brand-green: #9aa01e;
    --card-white: #f7f7f5;
    --ink-dark: #3a3a3a;
    --backdrop: #2d2e30;
  }
  * { box-sizing: border-box; margin: 0; padding: 0; }
  html, body {
    width: 1200px; height: 1000px; overflow: hidden;
    background: var(--backdrop);
    font-family: "Open Sans", sans-serif;
  }
  .canvas { position: relative; width: 1200px; height: 1000px; }

  .card {
    position: absolute;
    width: 525px; height: 300px;
    border-radius: 4px;
    overflow: hidden;
    box-shadow: 0 14px 30px rgba(0,0,0,.45);
  }
  .card--front { background: var(--card-white); }
  .card--back  { background: var(--brand-green); }

  .card--lena   { left: 50px;  top: 110px; }
  .card--marcus { left: 50px;  top: 570px; }
  .card--back   { left: 625px; top: 340px; }

  .contact {
    position: absolute; left: 255px; top: 46px;
    color: var(--ink-dark);
  }
  .contact__name {
    font-family: "Montserrat", sans-serif;
    font-weight: 700; font-size: 21px;
    color: var(--brand-green);
    line-height: 1.1;
  }
  .contact__role { font-size: 15px; margin-top: 2px; }
  .contact__lines { margin-top: 16px; font-size: 14px; line-height: 1.45; }
  .contact__label {
    display: inline-block; width: 30px;
    font-weight: 600; color: var(--brand-green);
  }

  .brand-band {
    position: absolute; left: 0; top: 212px;
    width: 320px; height: 60px;
    background: var(--brand-green);
    border-radius: 0 30px 30px 0;
    display: flex; align-items: center;
    padding-left: 24px; gap: 14px;
  }
  .brand-band__mark {
    flex: none;
    width: 36px; height: 36px; border-radius: 50%;
    border: 2.5px solid var(--card-white);
  }
  .brand-band__name {
    font-weight: 600; font-size: 23px; letter-spacing: .5px;
    color: var(--card-white); text-transform: uppercase;
    white-space: nowrap;
  }

  .web {
    position: absolute; right: 20px; top: 204px;
    display: flex; flex-direction: column; align-items: flex-end;
  }
  .web__url {
    font-size: 14px; color: var(--brand-green); font-weight: 400;
    white-space: nowrap; margin-bottom: 8px;
  }
  .web__icons { display: flex; gap: 6px; }
  .web__icon {
    width: 22px; height: 22px; border-radius: 5px;
    background: var(--brand-green);
  }

  .back__lockup {
    position: absolute; inset: 0;
    display: flex; flex-direction: column;
    align-items: center; justify-content: center; gap: 18px;
  }
  .back__mark {
    width: 110px; height: 110px; border-radius: 50%;
    border: 4px solid var(--card-white);
  }
  .back__name {
    font-weight: 600; font-size: 24px; letter-spacing: 1px;
    color: var(--card-white); text-transform: uppercase;
  }
</style>
</head>
<body>
<main class="canvas">

  <article class="card card--front card--lena">
    <div class="contact">
      <h2 class="contact__name">Lena Hartwell</h2>
      <p class="contact__role">Relationship Director</p>
      <p class="contact__lines">
        <span class="contact__label">M:</span>+44 7700 900 412<br>
        <span class="contact__label">E:</span>lh@copperridgehub.example
      </p>
    </div>
    <div class="brand-band">
      <span class="brand-band__mark"></span>
      <span class="brand-band__name">Copper Ridge</span>
    </div>
    <div class="web">
      <span class="web__url">copperridgehub.example</span>
      <div class="web__icons">
        <span class="web__icon"></span><span class="web__icon"></span><span class="web__icon"></span><span class="web__icon"></span><span class="web__icon"></span>
      </div>
    </div>
  </article>

  <article class="card card--front card--marcus">
    <div class="contact">
      <h2 class="contact__name">Marcus Dunmore</h2>
      <p class="contact__role">Founder &amp; Growth Hacker</p>
      <p class="contact__lines">
        <span class="contact__label">M:</span>+34 600 000 217<br>
        <span class="contact__label">E:</span>md@copperridgehub.example
      </p>
    </div>
    <div class="brand-band">
      <span class="brand-band__mark"></span>
      <span class="brand-band__name">Copper Ridge</span>
    </div>
    <div class="web">
      <span class="web__url">copperridgehub.example</span>
      <div class="web__icons">
        <span class="web__icon"></span><span class="web__icon"></span><span class="web__icon"></span><span class="web__icon"></span><span class="web__icon"></span>
      </div>
    </div>
  </article>

  <article class="card card--back">
    <div class="back__lockup">
      <span class="back__mark"></span>
      <span class="back__name">Copper Ridge</span>
    </div>
  </article>

</main>
</body>
</html>
```